Bref créative
Karvelo ApS wants a cool new identity on stationary
Total outline for the stationary stuff
Simple
Henrik Dahlquist
CEO
Birkeslette 218
5810 Naestved
Denmark
henrik@karvelo.dk
www.karvelo.dk
Free your mind
We want the design to show trust, technology, to be frontrunner, inovation etc. - streamlined with a crisp look.

```html
<!DOCTYPE html>
<html lang="en">
<head>
<meta charset="utf-8">
<title>Karvelo ApS – Stationery</title>
<link href="https://fonts.googleapis.com/css2?family=Ubuntu:wght@400;500;700&display=swap" rel="stylesheet">
<style>
:root{
  --green:#8dc63f;
  --green-dark:#6fa52a;
  --ink:#3a3a3a;
  --muted:#8a8a8a;
  --paper:#ffffff;
  --bg-light:#3a3a3a;
  --bg-dark:#141414;
  --label:#9a9a9a;
}
*{box-sizing:border-box;margin:0;padding:0}
html,body{width:1200px;height:586px;overflow:hidden}
body{font-family:"Ubuntu",sans-serif;color:var(--ink);position:relative}
.backdrop{position:absolute;inset:0;background:radial-gradient(ellipse at 50% 40%,var(--bg-light),var(--bg-dark) 75%)}
.brand{display:flex;align-items:center;gap:8px;font-weight:700;color:var(--ink);letter-spacing:-.3px;white-space:nowrap}
.brand .mark{width:14px;height:14px;background:var(--green);border-radius:2px;flex:none}
.label{position:absolute;font-size:9px;color:var(--label);text-align:center}
.contact{list-style:none;font-size:6.5px;line-height:10px;color:var(--muted);white-space:nowrap}
.contact li{display:flex;align-items:center;gap:4px}
.contact li::before{content:"";width:4px;height:4px;background:var(--green);border-radius:1px;flex:none}

/* business cards */
.card{position:absolute;width:199px;height:127px;background:var(--paper);border-radius:5px;overflow:hidden;box-shadow:0 4px 10px rgba(0,0,0,.5)}
.card .brand{position:absolute;font-size:22px}
.card .brand .mark{width:17px;height:17px}
.card .person{position:absolute;text-align:center;font-size:8px;line-height:11px;color:var(--green);font-weight:500;white-space:nowrap}
.card .person small{display:block;color:var(--muted);font-weight:400;font-size:6.5px;letter-spacing:.3px}
.card .address{position:absolute;font-size:6px;line-height:8px;color:var(--muted);white-space:nowrap}
.card .contact{position:absolute}

.card-one{left:84px;top:216px}
.card-one .brand{left:14px;top:14px}
.card-one .person{left:14px;top:60px;width:84px}
.card-one .address{left:28px;top:86px}
.card-one .contact{left:110px;top:62px}
.card-one .edge{position:absolute;right:0;top:62px;width:7px;height:48px;background:var(--green)}

.card-two{left:84px;top:379px}
.card-two .edge{position:absolute;left:0;top:12px;width:6px;height:26px;background:var(--green)}
.card-two .person{left:112px;top:12px;width:70px}
.card-two .address{left:118px;top:38px}
.card-two .contact{left:118px;top:56px}
.card-two .brand{left:14px;top:96px;font-size:20px}
.card-two .brand .mark{width:15px;height:15px}

/* letterhead */
.letterhead{position:absolute;left:300px;top:36px;width:276px;height:516px;background:var(--paper);box-shadow:0 6px 16px rgba(0,0,0,.55)}
.letterhead .brand{position:absolute;left:20px;top:34px;font-size:26px}
.letterhead .brand .mark{width:20px;height:20px}
.letterhead .address{position:absolute;left:148px;top:16px;font-size:6px;line-height:8px;color:var(--muted)}
.letterhead .contact{position:absolute;left:148px;top:34px}
.letterhead .footer{position:absolute;bottom:10px;width:100%;text-align:center;font-size:6px;color:var(--muted)}

/* big brand */
.hero{position:absolute;left:846px;top:68px}
.hero .brand{font-size:54px;color:#fff;gap:14px}
.hero .brand .mark{width:40px;height:40px;border-radius:4px}
.hero .tagline{margin-top:4px;padding-left:58px;font-size:11px;color:var(--label)}

/* envelopes */
.envelopes{position:absolute;left:690px;top:240px}
.envelope-front{position:absolute;left:6px;top:84px;width:420px;height:192px;background:var(--paper);box-shadow:0 6px 14px rgba(0,0,0,.55)}
.envelope-front .band{position:absolute;left:0;top:44px;width:150px;height:10px;background:var(--green)}
.envelope-front .brand{position:absolute;left:18px;top:60px;font-size:20px}
.envelope-front .brand .mark{width:14px;height:14px}
.envelope-front .address{position:absolute;left:46px;top:88px;font-size:5px;color:var(--muted)}
</style>
</head>
<body>
<div class="backdrop" role="img" aria-label="Dark wood-grain backdrop"></div>

<article class="card card-one">
  <div class="brand"><span class="mark"></span>Karvelo</div>
  <p class="person">Henrik Dahlquist<small>CEO</small></p>
  <p class="address">Birkeslette 218<br>5810 Naestved</p>
  <ul class="contact">
    <li>+45 2211 3344</li>
    <li>+45 2211 3345</li>
    <li>henrik@karvelo.dk</li>
    <li>www.karvelo.dk</li>
  </ul>
  <span class="edge"></span>
</article>
<p class="label" style="left:84px;top:352px;width:199px">Front Card Option 01</p>

<article class="card card-two">
  <span class="edge"></span>
  <p class="person">Henrik Dahlquist<small>CEO</small></p>
  <p class="address">Birkeslette 218<br>5810 Naestved</p>
  <ul class="contact">
    <li>+45 2211 3344</li>
    <li>+45 2211 3345</li>
    <li>henrik@karvelo.dk</li>
    <li>www.karvelo.dk</li>
  </ul>
  <div class="brand"><span class="mark"></span>Karvelo</div>
</article>
<p class="label" style="left:84px;top:515px;width:199px">Front Card Option 02</p>

<article class="letterhead">
  <div class="brand"><span class="mark"></span>Karvelo</div>
  <p class="address">Birkeslette 218<br>5810 Naestved, Denmark</p>
  <ul class="contact">
    <li>+45 2211 3344</li>
    <li>henrik@karvelo.dk</li>
  </ul>
  <p class="footer">www.karvelo.dk</p>
</article>
<p class="label" style="left:300px;top:561px;width:276px">Letterhead</p>

<div class="hero">
  <div class="brand"><span class="mark"></span>Karvelo</div>
  <p class="tagline">Stationary Concept</p>
</div>

<div class="envelopes">
  <svg width="500" height="290" viewBox="0 0 500 290" style="position:absolute;left:0;top:0">
    <g transform="rotate(-8 250 140)">
      <rect x="30" y="40" width="440" height="190" fill="#ffffff"/>
      <polygon points="30,40 470,40 250,150" fill="#8dc63f"/>
      <polygon points="30,40 470,40 250,118" fill="#7ab534"/>
      <rect x="236" y="122" width="16" height="16" rx="2" fill="#3a3a3a"/>
    </g>
  </svg>
  <div class="envelope-front">
    <svg width="420" height="192" viewBox="0 0 420 192" style="position:absolute;inset:0">
      <polyline points="0,0 210,100 420,0" fill="none" stroke="#e2e2e2" stroke-width="1.5"/>
      <polyline points="0,192 170,88" fill="none" stroke="#ececec" stroke-width="1"/>
      <polyline points="420,192 250,88" fill="none" stroke="#ececec" stroke-width="1"/>
    </svg>
    <span class="band"></span>
    <div class="brand"><span class="mark"></span>Karvelo</div>
    <p class="address">Birkeslette 218, 5810 Naestved</p>
  </div>
</div>
<p class="label" style="left:696px;top:552px;width:420px">Envelopes</p>
</body>
</html>
```